Business Card - The Harborline Group

We need a business card for a new venture capital fund and innovation accelerator based in San Francisco, CA. The Harborline Group will back, fund and scale life-transforming businesses. We intend to provide capital along with strategic and tactical direction to teams running exponential organizations. We are backing great ideas for vast markets with passionate visionaries. We facilitate the rapid creation of life-transforming businesses, help invent or re-invent critical industries and move the frontier of progress for the good of humankind. Maplecrest University defines Exponential Organizations as those whose impact (cost reduction or output) is disproportionally large – at least 10x larger – compared to its peers because of the use of new organizational techniques that leverage accelerating technologies. ExOs are characterized by a massive transformative purpose (MTP), a skunkworks organization and passionate teams of brilliant mountain-climbers with technical backgrounds.

Industry/Entity Type

Business

Contact Information for Business Card

Peter Odell
Managing Director

peter@theharborlinegroup.com
+1.628.307.4190

Font styles to use
Sans Serif

Requirements
Must have
• - logo
• - website: www.theharborlinegroup.com

```html
<!DOCTYPE html>
<html lang="en">
<head>
<meta charset="utf-8">
<title>The Harborline Group – Business Card</title>
<link rel="stylesheet" href="https://fonts.googleapis.com/css2?family=Roboto+Condensed:wght@400;700&display=swap">
<style>
  :root {
    --card-light: #ffffff;
    --card-mid: #ececec;
    --card-dark: #d6d6d6;
    --ink: #3a3a3a;
    --ink-soft: #8c8c8c;
    --brand: #3d78b5;
  }
  html, body {
    margin: 0;
    padding: 0;
    width: 686px;
    height: 1200px;
    overflow: hidden;
    background: #ffffff;
  }
  .card {
    position: relative;
    width: 686px;
    height: 1200px;
    overflow: hidden;
    font-family: "Roboto Condensed", "Arial Narrow", sans-serif;
    color: var(--ink);
    background:
      radial-gradient(ellipse 75% 40% at 65% 55%, var(--card-light) 0%, rgba(255,255,255,0) 70%),
      linear-gradient(160deg, var(--card-light) 0%, var(--card-mid) 45%, var(--card-dark) 75%, var(--card-mid) 100%);
  }
  .brand {
    position: absolute;
    left: 64px;
    top: 86px;
    width: 580px;
    height: 200px;
  }
  .brand-mark {
    position: absolute;
    left: 0;
    top: 20px;
    width: 136px;
    height: 136px;
    border-radius: 50%;
    background: var(--brand);
  }
  .brand-name {
    position: absolute;
    left: 156px;
    top: 8px;
    margin: 0;
    font-size: 58px;
    line-height: 56px;
    font-weight: 700;
    letter-spacing: 1px;
    text-transform: uppercase;
    color: var(--ink);
  }
  .brand-tagline {
    position: absolute;
    left: 156px;
    top: 186px;
    margin: 0;
    font-size: 15.5px;
    line-height: 19px;
    font-weight: 400;
    text-transform: uppercase;
    color: var(--ink-soft);
    letter-spacing: 0.3px;
  }
  .person {
    position: absolute;
    left: 0;
    width: 100%;
    top: 552px;
    text-align: center;
  }
  .person-name {
    margin: 0;
    font-size: 44px;
    line-height: 48px;
    font-weight: 700;
    text-transform: uppercase;
    color: var(--ink);
    letter-spacing: 0.5px;
  }
  .person-title {
    margin: 6px 0 0;
    font-size: 27px;
    line-height: 30px;
    font-weight: 400;
    text-transform: uppercase;
    color: var(--ink-soft);
  }
  .contact {
    position: absolute;
    left: 0;
    width: 100%;
    top: 1032px;
    text-align: center;
  }
  .contact-phone {
    margin: 0;
    font-size: 64px;
    line-height: 70px;
    font-weight: 700;
    color: var(--ink);
    letter-spacing: 1px;
  }
  .contact-web {
    margin: 14px 0 0;
    font-size: 28px;
    line-height: 32px;
    font-weight: 700;
    text-transform: uppercase;
    color: #111111;
  }
</style>
</head>
<body>
  <div class="card">
    <header class="brand">
      <div class="brand-mark" aria-hidden="true"></div>
      <h1 class="brand-name">The<br>Harborline<br>Group</h1>
      <p class="brand-tagline">Venture fund and innovation accelerator<br>for exponential technologies</p>
    </header>

    <section class="person">
      <h2 class="person-name">Peter Odell</h2>
      <p class="person-title">Managing Director</p>
    </section>

    <footer class="contact">
      <p class="contact-phone">1-628-307-4190</p>
      <p class="contact-web">www.theharborlinegroup.com</p>
    </footer>
  </div>
</body>
</html>
```